Elevating our current Business Card Design

We want to elevate our current business card with a new design to look like a marlow 800 company. We are a premium lubricant distributor (oil and grease).
We need 2 versions, version 1 is as per the uploaded a copy of our current business card with the English version.
For our Chinese version we need to use the front to be English in English and have the back of the card designed exactly like the front for all info to be in Chinese.
The design template needs to be such that we can amend the template with adding different information for each person's card.
The background colour of the card can be changed- we just need to clearly see all information on the card and logos.
The TRV and Verdant Mark logos cannot have any colour or display changes- only use the logos attached.
All logos need to be included and all information from the attached current card

```html
<!DOCTYPE html>
<html lang="en">
<head>
<meta charset="utf-8">
<title>Korvane Business Cards</title>
<link href="https://fonts.googleapis.com/css2?family=Montserrat:wght@400;500;700;800&family=Noto+Sans+SC:wght@400;700&display=swap" rel="stylesheet">
<style>
  :root {
    --bg: #d4d4d4;
    --card: #ffffff;
    --red: #e2231a;
    --deep-red: #b5161c;
    --rule: #a51d22;
    --ink: #4a4a4a;
    --grey: #9a9a9c;
    --green: #1f4d3a;
    --orange: #f28a1c;
  }
  * { box-sizing: border-box; margin: 0; padding: 0; }
  html, body { width: 1200px; height: 896px; overflow: hidden; }
  body {
    background: var(--bg);
    font-family: "Montserrat", sans-serif;
    color: var(--ink);
    position: relative;
  }
  .card {
    position: absolute;
    left: 337px;
    width: 525px;
    height: 300px;
    background: var(--card);
    border-radius: 26px;
    box-shadow: 0 10px 22px rgba(0,0,0,0.18);
  }
  .card--english { top: 126px; }
  .card--chinese { top: 475px; }
  .brand {
    position: absolute;
    left: 25px;
    top: 40px;
    display: flex;
    align-items: center;
    gap: 10px;
  }
  .brand-dot {
    width: 22px; height: 22px;
    border-radius: 50%;
    background: var(--orange);
  }
  .brand-name {
    font-weight: 800;
    font-size: 38px;
    letter-spacing: 1px;
    color: var(--red);
  }
  .tab {
    position: absolute;
    right: 0;
    top: 120px;
    width: 12px;
    height: 33px;
    background: var(--deep-red);
    border-radius: 8px 0 0 8px;
  }
  .identity {
    position: absolute;
    right: 25px;
    top: 115px;
    text-align: right;
  }
  .person-name {
    font-weight: 700;
    font-size: 19px;
    color: var(--deep-red);
    line-height: 24px;
  }
  .person-role {
    font-size: 14px;
    line-height: 20px;
    color: var(--ink);
  }
  .zh .person-name { font-family: "Noto Sans SC", sans-serif; font-size: 19px; letter-spacing: 1px; }
  .zh .person-role { font-family: "Noto Sans SC", sans-serif; font-size: 14px; }
  .rule {
    position: absolute;
    left: 25px; right: 24px;
    top: 167px;
    height: 1px;
    background: var(--rule);
  }
  .contacts {
    position: absolute;
    left: 25px;
    top: 179px;
    list-style: none;
  }
  .contacts li {
    display: flex;
    align-items: center;
    gap: 7px;
    height: 19.5px;
    font-size: 13.5px;
  }
  .contacts svg { width: 12px; height: 12px; fill: var(--red); flex: none; }
  .address {
    position: absolute;
    right: 25px;
    top: 179px;
    text-align: right;
    font-size: 13.5px;
    line-height: 19.5px;
  }
  .address.zh { font-family: "Noto Sans SC", sans-serif; }
  .badges {
    position: absolute;
    right: 25px;
    top: 230px;
    width: 230px;
    height: 40px;
  }
  .badge-partner {
    position: absolute;
    left: 2px; top: 26px;
    width: 107px; height: 17px;
    background: var(--red);
    border: 1px solid var(--red);
    transform: skewX(-8deg);
  }
  .badge-verdant {
    position: absolute;
    left: 128px; top: 4px;
    width: 44px; height: 36px;
    border-radius: 22px 22px 6px 6px;
    background: var(--green);
  }
  .badge-trv {
    position: absolute;
    left: 187px; top: -2px;
    width: 40px; height: 40px;
    border-radius: 50%;
    background: var(--orange);
  }
</style>
</head>
<body>

<section class="card card--english" aria-label="English business card">
  <div class="brand"><span class="brand-dot"></span><span class="brand-name">KORVANE</span></div>
  <div class="tab"></div>
  <div class="identity">
    <p class="person-name">MARISSA DOLAN</p>
    <p class="person-role">Administration Executive</p>
  </div>
  <div class="rule"></div>
  <ul class="contacts">
    <li><svg viewBox="0 0 12 12"><path d="M3 1 L5 3.5 L4 5 C4.8 6.6 5.6 7.4 7 8 L8.5 7 L11 9 L9.5 11 C5.5 10.5 1.5 6.5 1 2.5 Z"/></svg>1300 555 019</li>
    <li><svg viewBox="0 0 12 12"><path d="M3.5 0.5 H8.5 V11.5 H3.5 Z M4.5 1.8 V9.5 H7.5 V1.8 Z"/></svg>+61 400 555 217</li>
    <li><svg viewBox="0 0 12 12"><path d="M3 1 H9 V4 H3 Z M1 4.5 H11 V9 H9 V7 H3 V9 H1 Z M3.5 7.5 H8.5 V11 H3.5 Z"/></svg>+61 8 5550 1234</li>
    <li><svg viewBox="0 0 12 12"><path d="M1 3 H11 L6 6.5 Z M1 4 L6 7.5 L11 4 V10 H1 Z"/></svg>m.dolan@korvanedirect.com</li>
    <li><svg viewBox="0 0 12 12"><circle cx="6" cy="6" r="5.5"/></svg>www.korvanedirect.com</li>
  </ul>
  <div class="address">48 Harbour Freight Way<br>Redcliffe, WA 6104</div>
  <div class="badges">
    <div class="badge-partner" role="img" aria-label="Partner distributor badge"></div>
    <div class="badge-verdant" role="img" aria-label="Verdant Mark network member badge"></div>
    <div class="badge-trv" role="img" aria-label="TRV certification badge"></div>
  </div>
</section>

<section class="card card--chinese" aria-label="Chinese business card">
  <div class="brand"><span class="brand-dot"></span><span class="brand-name">KORVANE</span></div>
  <div class="tab"></div>
  <div class="identity zh">
    <p class="person-name">玛丽莎·多兰</p>
    <p class="person-role">行政主管</p>
  </div>
  <div class="rule"></div>
  <ul class="contacts">
    <li><svg viewBox="0 0 12 12"><path d="M3 1 L5 3.5 L4 5 C4.8 6.6 5.6 7.4 7 8 L8.5 7 L11 9 L9.5 11 C5.5 10.5 1.5 6.5 1 2.5 Z"/></svg>1300 555 019</li>
    <li><svg viewBox="0 0 12 12"><path d="M3.5 0.5 H8.5 V11.5 H3.5 Z M4.5 1.8 V9.5 H7.5 V1.8 Z"/></svg>+61 400 555 217</li>
    <li><svg viewBox="0 0 12 12"><path d="M3 1 H9 V4 H3 Z M1 4.5 H11 V9 H9 V7 H3 V9 H1 Z M3.5 7.5 H8.5 V11 H3.5 Z"/></svg>+61 8 5550 1234</li>
    <li><svg viewBox="0 0 12 12"><path d="M1 3 H11 L6 6.5 Z M1 4 L6 7.5 L11 4 V10 H1 Z"/></svg>m.dolan@korvanedirect.com</li>
    <li><svg viewBox="0 0 12 12"><circle cx="6" cy="6" r="5.5"/></svg>www.korvanedirect.com</li>
  </ul>
  <div class="address zh">港湾货运路48号<br>雷德克利夫, 华盛顿州 6104</div>
  <div class="badges">
    <div class="badge-partner" role="img" aria-label="Partner distributor badge"></div>
    <div class="badge-verdant" role="img" aria-label="Verdant Mark network member badge"></div>
    <div class="badge-trv" role="img" aria-label="TRV certification badge"></div>
  </div>
</section>

</body>
</html>
```